Crestline Marketing Business Card

Business card using new logo for marketing consulting company based in Silicon Valley. Limited information on card now (name, phone number, email, website), but room to add mailing address later.

```html
<!DOCTYPE html>
<html lang="en">
<head>
<meta charset="utf-8">
<title>Crestline Marketing Business Card</title>
<link href="https://fonts.googleapis.com/css2?family=Exo+2:wght@300;400;500&display=swap" rel="stylesheet">
<style>
  :root {
    --page: #ececec;
    --card-white: #ffffff;
    --navy: #1b3461;
    --navy-deep: #1a3159;
    --teal-glow: #0a6b98;
    --sky: #2bb5e8;
    --ink: #1e3160;
    --name-grey: #4a4a4a;
    --title-grey: #9a9a9a;
    --white: #ffffff;
  }
  * { box-sizing: border-box; margin: 0; padding: 0; }
  html, body { width: 1200px; height: 1200px; overflow: hidden; }
  body {
    background: var(--page);
    font-family: "Exo 2", sans-serif;
    position: relative;
  }
  .card { position: absolute; box-shadow: 0 6px 14px rgba(0,0,0,0.18); overflow: hidden; }

  /* Front */
  .card-front {
    left: 268px; top: 119px; width: 661px; height: 427px;
    background: var(--card-white);
  }
  .front-band {
    position: absolute; left: 0; right: 0; bottom: 0; height: 9px;
    background: linear-gradient(90deg, var(--navy) 0%, #1f6fa8 40%, var(--sky) 55%, #1f6fa8 70%, var(--navy) 100%);
  }
  .person { position: absolute; left: 25px; top: 135px; }
  .person-name { font-size: 30px; font-weight: 400; color: var(--name-grey); line-height: 1; }
  .person-title { font-size: 20px; font-weight: 300; color: var(--title-grey); margin-top: 9px; line-height: 1; }

  .contact-row {
    display: flex; align-items: center; gap: 14px;
    font-size: 21px; color: var(--ink); line-height: 1; white-space: nowrap;
  }
  .contact-row svg { width: 26px; height: 24px; flex: none; }

  .personal-contacts {
    position: absolute; left: 22px; top: 236px;
    display: flex; flex-direction: column; gap: 14px;
  }
  .company-contacts {
    position: absolute; right: 20px; top: 226px;
    display: flex; flex-direction: column; gap: 16px;
  }
  .address-row { position: absolute; right: 20px; top: 379px; }
  .address-row svg { width: 32px; height: 26px; }

  .brand-mark {
    position: absolute; right: 20px; top: 20px; width: 250px;
    display: flex; flex-direction: column; align-items: center;
  }
  .brand-dot { width: 74px; height: 74px; border-radius: 50%; background: var(--sky); }
  .brand-name {
    margin-top: 26px; font-size: 27px; font-weight: 400; color: var(--sky);
    line-height: 1; white-space: nowrap;
  }

  /* Back */
  .card-back {
    left: 270px; top: 570px; width: 656px; height: 424px;
    background: radial-gradient(circle at 50% 40%, var(--teal-glow) 0%, #0d4a7a 30%, var(--navy-deep) 62%);
  }
  .back-brand {
    position: absolute; left: 0; right: 0; top: 100px;
    display: flex; flex-direction: column; align-items: center;
  }
  .back-brand .brand-dot { width: 110px; height: 110px; background: var(--white); }
  .back-brand .brand-name { color: var(--white); font-size: 42px; margin-top: 42px; }
</style>
</head>
<body>

<section class="card card-front" aria-label="Business card front">
  <div class="person">
    <p class="person-name">Daniel Reyes</p>
    <p class="person-title">Creative Designer</p>
  </div>

  <div class="personal-contacts">
    <div class="contact-row">
      <svg viewBox="0 0 24 24" aria-hidden="true"><path fill="#2bb5e8" d="M6.6 2.5l3 3.8-1.8 2.4c1.2 2.6 3.2 4.7 5.8 6l2.4-1.8 3.8 3-1.8 3.4C10.6 19 4.8 13.2 4 4.4z"/></svg>
      <span>+1-415 -555-0142</span>
    </div>
    <div class="contact-row">
      <svg viewBox="0 0 26 20" aria-hidden="true"><rect x="1" y="1.5" width="24" height="17" fill="none" stroke="#2bb5e8" stroke-width="1.8"/><path d="M1.5 2l11.5 10 11.5-10M1.5 18l8.5-8M24.5 18l-8.5-8" fill="none" stroke="#2bb5e8" stroke-width="1.6"/></svg>
      <span>dreyes@crestline-mkt.us</span>
    </div>
  </div>

  <div class="brand-mark">
    <div class="brand-dot"></div>
    <p class="brand-name">Crestline Marketing</p>
  </div>

  <div class="company-contacts">
    <div class="contact-row">
      <svg viewBox="0 0 26 24" aria-hidden="true"><path fill="#2bb5e8" d="M2 8c3-5 19-5 22 0l-1 3h-4l-1-3H8l-1 3H3zM6 11h14l3 10H3z"/><circle cx="13" cy="16" r="2.5" fill="#fff"/></svg>
      <span>+1-415 -555-0176</span>
    </div>
    <div class="contact-row">
      <svg viewBox="0 0 26 24" aria-hidden="true"><rect x="7" y="1" width="12" height="6" fill="#2bb5e8"/><rect x="2" y="8" width="22" height="9" rx="2" fill="#2bb5e8"/><rect x="7" y="14" width="12" height="9" fill="#fff" stroke="#2bb5e8" stroke-width="1.8"/></svg>
      <span>+1-415 -555-0177</span>
    </div>
    <div class="contact-row">
      <svg viewBox="0 0 24 24" aria-hidden="true"><g fill="none" stroke="#2bb5e8" stroke-width="1.4"><circle cx="12" cy="12" r="10.5"/><ellipse cx="12" cy="12" rx="4.5" ry="10.5"/><path d="M1.5 12h21M3 7h18M3 17h18"/></g></svg>
      <span>www.crestline-mkt.us</span>
    </div>
    <div class="contact-row">
      <svg viewBox="0 0 26 20" aria-hidden="true"><rect x="1" y="1.5" width="24" height="17" fill="none" stroke="#2bb5e8" stroke-width="1.8"/><path d="M1.5 2l11.5 10 11.5-10M1.5 18l8.5-8M24.5 18l-8.5-8" fill="none" stroke="#2bb5e8" stroke-width="1.6"/></svg>
      <span>hello@crestline-mkt.us</span>
    </div>
  </div>

  <div class="contact-row address-row">
    <svg viewBox="0 0 30 26" aria-hidden="true"><path d="M2 13L15 2l13 11M6 10v14h7v-7h4v7h7V10" fill="none" stroke="#2bb5e8" stroke-width="2.6" stroke-linejoin="round"/></svg>
    <span>2150, Alder Ln, San Jose, CA 95128.</span>
  </div>

  <div class="front-band"></div>
</section>

<section class="card card-back" aria-label="Business card back">
  <div class="back-brand">
    <div class="brand-dot"></div>
    <p class="brand-name">Crestline Marketing</p>
  </div>
</section>

</body>
</html>
```